Buchverlag sucht Cover-Design
Zielgruppe
Wir sind ein Buchverlag, der über Bravolo publizieren.
Unsere Zielgruppe sind: alle Selbstständigen, Unternehmern, Intrapreneuren, genauso wie Coaches, Experten, Start-ups und Entrepreneure.
Auch an diejenigen, die dieses Vorhaben angehen möchten.
Aufgabenstellung
Das Cover soll Nischen entsprechend sein. (Business Findung und Gestaltung)
Andersartig, auffallend, jedoch seriös sein.
Genaue Vorstellung:
Ein im freien Naturlandschaft fliegender Adler, der seine Beute fest im Blick hat und zielgenau seine Beute
zugreifen kann!
Den Schriftzug auffällig gestalten
Titel:
HOHE WARTE - Echter Reichtum gehört jedem von Anfang an
Untertitel:
Die klare Haltung der Vorreiter mit praktischem Wegweiser für Klarheit & Zufriedenheit bei privaten und beruflichen Weichenstellungen
Autor:
Velina Korbach
Logo des Verlags im Anhang
Name des Verlags:
Mond Quelle Verlag

```html
<!DOCTYPE html>
<html lang="de">
<head>
<meta charset="utf-8">
<title>Hohe Warte – Buchcover</title>
<link rel="stylesheet" href="https://fonts.googleapis.com/css2?family=Playfair+Display:wght@400&family=Source+Sans+3:wght@400;600;700&display=swap">
<style>
  :root {
    --sky-top: #86afdb;
    --sky-low: #bcd6ee;
    --rock-light: #b8aa9b;
    --rock: #9a8a7b;
    --rock-dark: #6f6358;
    --forest: #4d6a2c;
    --forest-dark: #24341a;
    --lake: #34c2b8;
    --lake-deep: #1fa39c;
    --accent: #f7b43a;
    --text-light: #ffffff;
  }
  * { margin: 0; padding: 0; box-sizing: border-box; }
  html, body { width: 848px; height: 1200px; overflow: hidden; background: #ffffff; }
  .cover {
    position: relative;
    width: 848px;
    height: 1200px;
    overflow: hidden;
    font-family: "Source Sans 3", sans-serif;
    color: var(--text-light);
  }
  .cover__landscape {
    position: absolute;
    inset: 0;
    background:
      radial-gradient(ellipse 420px 360px at 760px 700px, rgba(61,88,36,0.95) 0%, rgba(61,88,36,0.6) 55%, rgba(61,88,36,0) 100%),
      radial-gradient(ellipse 520px 160px at 300px 840px, rgba(36,52,26,0.85) 0%, rgba(36,52,26,0) 100%),
      linear-gradient(180deg,
        var(--sky-top) 0%,
        var(--sky-low) 22%,
        var(--rock-light) 30%,
        var(--rock) 45%,
        var(--rock-dark) 62%,
        var(--forest) 70%,
        var(--forest-dark) 72.5%,
        var(--lake) 74.5%,
        var(--lake-deep) 100%);
  }
  .cover__author {
    position: absolute;
    left: 45px;
    top: 24px;
    font-size: 40px;
    font-weight: 600;
    color: var(--accent);
    line-height: 1;
  }
  .cover__title {
    position: absolute;
    left: 46px;
    top: 62px;
    font-family: "Playfair Display", serif;
    font-weight: 400;
    font-size: 192px;
    line-height: 158px;
    letter-spacing: -4px;
  }
  .cover__title span { display: block; }
  .cover__tagline {
    position: absolute;
    left: 52px;
    top: 408px;
    font-size: 28px;
    font-weight: 400;
    text-transform: uppercase;
    text-shadow: 0 1px 3px rgba(0,0,0,0.25);
  }
  .cover__subtitle {
    position: absolute;
    left: 52px;
    top: 690px;
    width: 770px;
    font-size: 36px;
    font-weight: 400;
    line-height: 48px;
    text-shadow: 0 1px 4px rgba(0,0,0,0.35);
  }
  .publisher {
    position: absolute;
    left: 352px;
    top: 1124px;
    display: flex;
    align-items: center;
    gap: 12px;
  }
  .publisher__dot {
    width: 36px;
    height: 36px;
    border-radius: 50%;
    background: var(--accent);
  }
  .publisher__name {
    font-size: 56px;
    font-weight: 700;
    color: var(--accent);
    line-height: 1;
  }
</style>
</head>
<body>
  <main class="cover">
    <div class="cover__landscape" role="img" aria-label="Alpine Berglandschaft mit Felsgipfeln, Nadelwald und türkisem See mit Ruderboot, ein fliegender Adler und ein Leopard auf dem Gipfel"></div>
    <p class="cover__author">Velina Korbach</p>
    <h1 class="cover__title"><span>HOHE</span><span>WARTE</span></h1>
    <p class="cover__tagline">Echter Reichtum gehört jedem von Anfang an</p>
    <p class="cover__subtitle">Die klare Haltung der Vorreiter mit praktischem Wegweiser für Klarheit &amp; Zufriedenheit bei privaten und beruflichen Weichenstellungen</p>
    <div class="publisher">
      <span class="publisher__dot"></span>
      <span class="publisher__name">MQV</span>
    </div>
  </main>
</body>
</html>
```